Business Card, A4 Letter Head and DL Envelope for Vantrelle

We are looking for a design for our Business Card, A4 Letter Head and DL Envelope.

Vantrelle is a distributor of promotional products. We specialize in a range of branded promotional products, these include pens, polo shirts, key rings, drink bottles, uniforms and bags to name a few. We are experts in marketing and assist companies in choosing the right promotional product for their needs. We will predominately be an online business where customers visit our website and browse our range of promotional products and branding options.

Our colours are black, red, white and grey.

Files must be supplied in eps, pdf and ai format.

Please display the following information:
Corbin Hale
Account Manager
Suite xxx, 214 Dawlish Parade Melbourne, Victoria 3000
Phone +61 3 5550 1827
Mobile +61 455 501 936
sales@vantrelle.com.au
www.vantrelle.com.au

```html
<!DOCTYPE html>
<html lang="en">
<head>
<meta charset="utf-8">
<title>Vantrelle Stationery Set</title>
<link rel="stylesheet" href="https://fonts.googleapis.com/css2?family=Exo+2:wght@700&family=Open+Sans:wght@400;600&family=Great+Vibes&display=swap">
<style>
  :root {
    --red: #d3151c;
    --red-deep: #8e0d12;
    --red-mid: #b8141a;
    --black: #1c1c1c;
    --charcoal: #2e2e2e;
    --grey: #8a8a8a;
    --grey-light: #d9d9d9;
    --white: #ffffff;
    --ink: #333333;
    --stage: #ebe8e4;
  }
  * { box-sizing: border-box; margin: 0; padding: 0; }
  html, body { width: 1200px; height: 1024px; overflow: hidden; }
  body { background: var(--stage); font-family: "Open Sans", Arial, sans-serif; color: var(--ink); position: relative; }

  .piece { position: absolute; overflow: hidden; box-shadow: 0 2px 6px rgba(0,0,0,.18); }
  .brand-name { font-family: "Exo 2", Arial, sans-serif; font-weight: 700; text-transform: uppercase; letter-spacing: .5px; line-height: 1; }
  .brand-mark { display: flex; align-items: center; gap: 8px; }
  .brand-dot { border-radius: 50%; background: var(--red); flex: none; }
  .swoosh { position: absolute; left: 0; bottom: 0; width: 100%; }
  .decor-area { position: absolute; }

  .contact { font-size: 6.5px; line-height: 1.45; color: #555; }
  .contact-line { display: flex; align-items: center; gap: 3px; }
  .contact-line svg { width: 6px; height: 6px; flex: none; }

  /* Letterhead */
  .letterhead { left: 32px; top: 30px; width: 343px; height: 483px; background: var(--white); }
  .letterhead .brand-mark { position: absolute; left: 18px; top: 42px; }
  .letterhead .brand-name { font-size: 15px; color: var(--charcoal); }
  .letterhead .brand-dot { width: 14px; height: 14px; }
  .letterhead .contact { position: absolute; left: 205px; top: 30px; border-left: 1px solid var(--grey-light); padding-left: 5px; }
  .letter-body { position: absolute; left: 18px; top: 124px; width: 308px; font-size: 5.6px; line-height: 1.5; color: #555; }
  .letter-body .salutation { font-size: 7px; color: var(--ink); margin-bottom: 7px; }
  .letter-body p { margin-bottom: 6px; }
  .signature { font-family: "Great Vibes", cursive; font-size: 13px; color: var(--ink); margin-top: 10px; }
  .signature-role { font-size: 5.5px; color: #555; }
  .web { position: absolute; font-size: 7px; color: var(--white); }
  .letterhead .web { right: 20px; bottom: 12px; }

  /* Covers */
  .cover { top: 30px; height: 484px; }
  .cover-red { left: 418px; width: 312px; background: radial-gradient(circle at 45% 45%, #e32028 0%, var(--red-mid) 45%, var(--red-deep) 100%); }
  .cover-black { left: 808px; width: 344px; background: radial-gradient(circle at 50% 35%, #2c2c2c 0%, #141414 70%, #0a0a0a 100%); }
  .cover .brand-mark { position: absolute; top: 96px; left: 0; width: 100%; justify-content: center; }
  .cover .brand-name { font-size: 22px; }
  .cover .brand-dot { width: 18px; height: 18px; }
  .cover-red .brand-name { color: var(--white); }
  .cover-red .brand-dot { background: var(--white); }
  .cover-black .brand-name { color: var(--grey-light); }
  .cover .decor-area { left: 70px; top: 170px; width: 270px; height: 300px; border-radius: 8px; }
  .cover-red .decor-area { background: radial-gradient(ellipse at 40% 30%, rgba(255,255,255,.22), rgba(255,255,255,0) 70%); }
  .cover-black .decor-area { background: radial-gradient(ellipse at 40% 35%, rgba(150,150,150,.45), rgba(110,80,70,.25) 50%, rgba(0,0,0,0) 75%); }
  .cover .web { left: 0; width: 100%; text-align: center; bottom: 18px; font-size: 8px; }

  /* Business cards */
  .card { top: 544px; height: 173px; border-radius: 14px; }
  .card-front { left: 56px; width: 330px; background: var(--white); }
  .card-front .brand-mark { position: absolute; left: 20px; top: 56px; }
  .card-front .brand-name { font-size: 15px; color: var(--charcoal); }
  .card-front .brand-dot { width: 12px; height: 12px; }
  .card-person { position: absolute; left: 18px; bottom: 14px; color: var(--white); font-size: 7.5px; line-height: 1.35; }
  .card-person .person-name { text-transform: uppercase; font-size: 8.5px; font-weight: 600; }
  .card-front .contact { position: absolute; left: 172px; bottom: 12px; color: var(--white); font-size: 7px; }

  .card-dark { left: 438px; top: 547px; height: 170px; width: 296px; background: linear-gradient(160deg, #3a3a3a, #1d1d1d 60%, #111); }
  .card-red { left: 833px; width: 317px; background: radial-gradient(circle at 35% 40%, #e32028, var(--red-mid) 50%, var(--red-deep)); }
  .card .decor-area { left: 0; top: 0; width: 150px; height: 100%; }
  .card-dark .decor-area { background: radial-gradient(ellipse at 40% 40%, rgba(200,200,200,.35), rgba(180,20,25,.25) 45%, rgba(0,0,0,0) 75%); }
  .card-red .decor-area { background: radial-gradient(ellipse at 40% 40%, rgba(255,255,255,.3), rgba(255,255,255,0) 70%); }
  .card-back-brand { position: absolute; right: 18px; top: 96px; text-align: left; }
  .card-back-brand .brand-name { font-size: 16px; }
  .card-back-brand .web { position: static; font-size: 7px; margin-top: 3px; }
  .card-dark .brand-name { color: var(--white); }
  .card-dark .web { color: #bbb; }
  .card-red .brand-name { color: var(--white); }

  /* Envelopes */
  .envelope { top: 744px; height: 252px; }
  .envelope-front { left: 13px; width: 368px; background: var(--white); }
  .envelope-front .brand-mark { position: absolute; left: 20px; top: 70px; }
  .envelope-front .brand-name { font-size: 15px; color: var(--charcoal); }
  .envelope-front .brand-dot { width: 12px; height: 12px; }
  .envelope-front .contact { position: absolute; left: 242px; top: 36px; }
  .address-window { position: absolute; left: 18px; top: 114px; width: 142px; height: 46px; border: 1px solid #c9c9c9; border-radius: 5px; background: linear-gradient(#f3f3f3, #e6e6e6); }
  .envelope-front .web { right: 20px; bottom: 10px; }

  .envelope-back { top: 742px; height: 254px; }
  .envelope-back-white { left: 403px; width: 373px; background: var(--white); }
  .envelope-back-red { left: 799px; width: 377px; background: radial-gradient(circle at 55% 45%, #c8161d, var(--red-mid) 45%, var(--red-deep)); }
  .flap { position: absolute; left: 0; top: 0; width: 100%; height: 80px; }
  .envelope-back .brand-mark { position: absolute; top: 32px; left: 0; width: 100%; justify-content: center; gap: 5px; }
  .envelope-back .brand-name { font-size: 9px; }
  .envelope-back .brand-dot { width: 8px; height: 8px; }
  .envelope-back-white .brand-name { color: var(--white); }
  .envelope-back-white .brand-dot { background: var(--white); }
  .envelope-back-red .brand-name { color: var(--white); }
  .envelope-back-red .brand-dot { background: var(--white); }
  .envelope-back .decor-area { left: 90px; top: 70px; width: 260px; height: 170px; border-radius: 8px; }
  .envelope-back-white .decor-area { background: radial-gradient(ellipse at 50% 45%, rgba(225,225,225,.9), rgba(240,200,190,.45) 50%, rgba(255,255,255,0) 78%); }
  .envelope-back-red .decor-area { background: radial-gradient(ellipse at 45% 40%, rgba(255,255,255,.18), rgba(255,255,255,0) 70%); }
  .envelope-back .web { left: 0; width: 100%; text-align: center; bottom: 10px; }
  .envelope-back-white .web { color: var(--red); }
</style>
</head>
<body>

<!-- A4 letterhead -->
<section class="piece letterhead">
  <div class="brand-mark"><span class="brand-dot"></span><span class="brand-name">Vantrelle</span></div>
  <div class="contact">
    <div class="contact-line"><svg viewBox="0 0 6 6"><rect x="1" y="0.5" width="4" height="5" rx="1" fill="#d3151c"/></svg>+61 3 5550 1827</div>
    <div class="contact-line"><svg viewBox="0 0 6 6"><rect x="1.5" y="0" width="3" height="6" rx=".6" fill="#d3151c"/></svg>+61 455 501 936</div>
    <div class="contact-line"><svg viewBox="0 0 6 6"><rect x="0" y="1" width="6" height="4" fill="#d3151c"/></svg>sales@vantrelle.com.au</div>
    <div>Suite xxx, 214 Dawlish Parade</div>
    <div>Melbourne, Victoria 3000</div>
  </div>
  <div class="letter-body">
    <div class="salutation">Lorem Ipsum,</div>
    <p>Thank you for your interest in our range of branded products. We help businesses choose items that carry their name well and suit every budget, event and audience across the country.</p>
    <p>Our team reviews each order with care, checks every proof and keeps you informed from the first quote until delivery reaches your door.</p>
    <p>Pens, polo shirts, key rings, drink bottles, uniforms and bags can all be printed or embroidered with your colours and logo in short lead times.</p>
    <p>Browse our website to compare branding options, request samples and place repeat orders whenever your next campaign needs fresh stock.</p>
    <p>Please contact us with any questions about pricing or availability.</p>
    <p>We look forward to working with you.</p>
    <div class="signature">Yours Name</div>
    <div class="signature-role">Company Director</div>
  </div>
  <svg class="swoosh" viewBox="0 0 343 80" preserveAspectRatio="none" height="80">
    <path d="M0 40 C110 20 230 18 343 22 L343 80 L0 80 Z" fill="#9a9a9a"/>
    <path d="M0 48 C110 30 230 28 343 30 L343 80 L0 80 Z" fill="#1c1c1c"/>
    <path d="M0 58 C110 42 230 38 343 40 L343 80 L0 80 Z" fill="#d3151c"/>
  </svg>
  <div class="web">www.vantrelle.com.au</div>
</section>

<!-- Red folder cover -->
<section class="piece cover cover-red">
  <div class="brand-mark"><span class="brand-dot"></span><span class="brand-name">Vantrelle</span></div>
  <div class="decor-area" role="img" aria-label="Large soft brand decoration in red and white tones"></div>
  <div class="web">www.vantrelle.com.au</div>
</section>

<!-- Black folder cover -->
<section class="piece cover cover-black">
  <div class="brand-mark"><span class="brand-dot"></span><span class="brand-name">Vantrelle</span></div>
  <div class="decor-area" role="img" aria-label="Large soft brand decoration in grey and bronze tones"></div>
  <div class="web">www.vantrelle.com.au</div>
</section>

<!-- Business card front -->
<section class="piece card card-front">
  <div class="brand-mark"><span class="brand-dot"></span><span class="brand-name">Vantrelle</span></div>
  <svg class="swoosh" viewBox="0 0 330 80" preserveAspectRatio="none" height="80">
    <path d="M0 18 C100 6 220 4 330 8 L330 80 L0 80 Z" fill="#9a9a9a"/>
    <path d="M0 24 C100 12 220 10 330 14 L330 80 L0 80 Z" fill="#1c1c1c"/>
    <path d="M0 30 C100 20 220 18 330 20 L330 80 L0 80 Z" fill="#c0141a"/>
  </svg>
  <div class="card-person">
    <div class="person-name">Corbin Hale</div>
    <div>Account Manager</div>
    <div>www.vantrelle.com.au</div>
  </div>
  <div class="contact">
    <div class="contact-line"><svg viewBox="0 0 6 6"><rect x="1" y="0.5" width="4" height="5" rx="1" fill="#fff"/></svg>+61 3 5550 1827</div>
    <div class="contact-line"><svg viewBox="0 0 6 6"><rect x="1.5" y="0" width="3" height="6" rx=".6" fill="#fff"/></svg>+61 455 501 936</div>
    <div class="contact-line"><svg viewBox="0 0 6 6"><rect x="0" y="1" width="6" height="4" fill="#fff"/></svg>sales@vantrelle.com.au</div>
    <div>Suite xxx, 214 Dawlish Parade</div>
    <div>Melbourne, Victoria 3000</div>
  </div>
</section>

<!-- Business card back, dark -->
<section class="piece card card-dark">
  <div class="decor-area" role="img" aria-label="Brand decoration in silver and red tones"></div>
  <div class="card-back-brand">
    <div class="brand-name">Vantrelle</div>
    <div class="web">www.vantrelle.com.au</div>
  </div>
</section>

<!-- Business card back, red -->
<section class="piece card card-red">
  <div class="decor-area" role="img" aria-label="Brand decoration in silver and red tones"></div>
  <div class="card-back-brand">
    <div class="brand-name">Vantrelle</div>
    <div class="web">www.vantrelle.com.au</div>
  </div>
</section>

<!-- DL envelope front -->
<section class="piece envelope envelope-front">
  <div class="brand-mark"><span class="brand-dot"></span><span class="brand-name">Vantrelle</span></div>
  <div class="contact">
    <div class="contact-line"><svg viewBox="0 0 6 6"><rect x="1" y="0.5" width="4" height="5" rx="1" fill="#d3151c"/></svg>+61 3 5550 1827</div>
    <div class="contact-line"><svg viewBox="0 0 6 6"><rect x="1.5" y="0" width="3" height="6" rx=".6" fill="#d3151c"/></svg>+61 455 501 936</div>
    <div class="contact-line"><svg viewBox="0 0 6 6"><rect x="0" y="1" width="6" height="4" fill="#d3151c"/></svg>sales@vantrelle.com.au</div>
    <div>Suite xxx, 214 Dawlish Parade</div>
    <div>Melbourne, Victoria 3000</div>
  </div>
  <div class="address-window"></div>
  <svg class="swoosh" viewBox="0 0 368 60" preserveAspectRatio="none" height="60">
    <path d="M0 18 C120 10 250 8 368 10 L368 60 L0 60 Z" fill="#9a9a9a"/>
    <path d="M0 24 C120 16 250 14 368 16 L368 60 L0 60 Z" fill="#1c1c1c"/>
    <path d="M0 32 C120 24 250 20 368 22 L368 60 L0 60 Z" fill="#d3151c"/>
  </svg>
  <div class="web">www.vantrelle.com.au</div>
</section>

<!-- DL envelope back, white -->
<section class="piece envelope envelope-back envelope-back-white">
  <svg class="flap" viewBox="0 0 373 80" preserveAspectRatio="none">
    <path d="M0 0 L373 0 L373 14 C300 40 240 76 186 78 C132 76 72 40 0 14 Z" fill="#c0141a"/>
  </svg>
  <div class="brand-mark"><span class="brand-dot"></span><span class="brand-name">Vantrelle</span></div>
  <div class="decor-area" role="img" aria-label="Faint brand decoration in pale grey and blush tones"></div>
  <div class="web">www.vantrelle.com.au</div>
</section>

<!-- DL envelope back, red -->
<section class="piece envelope envelope-back envelope-back-red">
  <svg class="flap" viewBox="0 0 377 80" preserveAspectRatio="none">
    <path d="M0 0 L377 0 L377 14 C300 40 240 76 188 78 C136 76 76 40 0 14 Z" fill="#a51118"/>
    <path d="M0 14 C76 40 136 76 188 78 C240 76 300 40 377 14" fill="none" stroke="#7a0c10" stroke-width="1"/>
  </svg>
  <div class="brand-mark"><span class="brand-dot"></span><span class="brand-name">Vantrelle</span></div>
  <div class="decor-area" role="img" aria-label="Faint brand decoration in light red tones"></div>
  <div class="web">www.vantrelle.com.au</div>
</section>

</body>
</html>
```